Home Page Website Design

The Site width is 1000 px. I've attached a Balsamiq mockup as a design layout guide. The design needs to be flat and clean. Please stick to the pixel dimensions of the mock up as the site will be responsive. I've also attached the logos used on the mockup for positional purposes.

Colours to use: Black, Grey, Green (Logo tie in) & green complementary colours.

Green (Logo tie in)
White Background
Titles: Black (Roboto Bold 700)
Text: Dark Grey (Roboto Normal 400)

Look & Style Example
http://www.brindlowlearn.org.uk/

Type Face
Google Fonts - Roboto

These are just guidelines, please feel free to use you own creative judgment.

Thanks

```html
<!DOCTYPE html>
<html lang="en">
<head>
<meta charset="utf-8">
<title>Marlow Vale Teaching Alliance – Home</title>
<link href="https://fonts.googleapis.com/css2?family=Roboto:wght@400;700&family=Roboto+Condensed:wght@400;700&display=swap" rel="stylesheet">
<style>
:root{
  --green:#3cb46e;
  --green-dark:#2f9a5b;
  --green-pale:#d9f0e2;
  --ink:#1e1e1e;
  --text:#3a3a3a;
  --grey-dark:#444;
  --grey-mid:#8a8a8a;
  --grey-line:#d4d4d4;
  --page-grey:#ececec;
  --panel:#f6f6f6;
  --white:#fff;
}
*{box-sizing:border-box;margin:0;padding:0}
html,body{width:900px;height:1200px;overflow:hidden}
body{position:relative;background:var(--white);font-family:"Roboto",Arial,sans-serif;color:var(--text)}
.abs{position:absolute}

/* header */
.brand{left:108px;top:14px;width:150px;color:var(--green);font:700 17px/1.15 "Roboto",sans-serif}
.brand-mark{display:inline-block;width:14px;height:14px;background:var(--green);margin-bottom:6px}
.search-label{left:289px;top:34px;font:700 10.5px "Roboto",sans-serif;color:var(--ink)}
.search-box{left:284px;top:48px;width:169px;height:25px;border:1px solid var(--grey-line);background:#f2f2f2}
.search-box svg{position:absolute;right:8px;top:5px}
.live-chat{left:478px;top:14px;width:66px;text-align:center;font:400 13px "Roboto",sans-serif;color:var(--ink)}
.live-chat svg{display:block;margin:0 auto 2px}
.not-member{left:573px;top:36px;font:400 7.5px "Roboto",sans-serif;color:var(--ink)}
.register{left:644px;top:33px;font:400 11px "Roboto",sans-serif;color:var(--ink)}
.btn-login{left:744px;top:16px;width:55px;height:23px;background:var(--grey-dark);color:var(--white);font:700 9px/23px "Roboto",sans-serif;text-align:center}
.email-box{left:571px;top:49px;width:165px;height:24px;background:#f2f2f2;border:1px solid var(--grey-line);font:400 8.5px/22px "Roboto",sans-serif;padding-left:6px;color:var(--ink)}
.btn-submit{left:744px;top:49px;width:55px;height:24px;background:var(--green);color:var(--white);font:700 9px/24px "Roboto",sans-serif;text-align:center}
.top-deco{left:640px;top:0}

/* nav */
.main-nav{left:97px;top:87px;width:706px;height:34px;border-top:1px solid var(--grey-line)}
.main-nav a{position:absolute;top:11px;font:400 10.5px "Roboto",sans-serif;color:var(--ink);text-decoration:none;white-space:nowrap}
.main-nav a.active{color:var(--green)}

/* hero */
.page-band{left:0;top:389px;width:900px;height:491px;background:var(--page-grey)}
.hero-panel{left:97px;top:123px;width:303px;height:266px;background:var(--green)}
.hero-dots{left:108px;top:129px;display:flex;gap:3px}
.hero-dots span{width:8px;height:8px;border-radius:50%;background:var(--grey-dark)}
.hero-dots span.on{background:var(--white)}
.hero-title{left:113px;top:157px;width:280px;color:var(--white);font:700 17.5px "Roboto Condensed",sans-serif}
.hero-copy{left:113px;top:185px;width:275px;color:var(--white);font:700 10.5px/1.38 "Roboto",sans-serif}
.hero-more{left:115px;top:298px;color:var(--white);font:700 10px "Roboto",sans-serif}
.hero-photo{left:400px;top:123px;width:403px;height:266px;background:linear-gradient(135deg,#d7d2c8 0%,#8f8a84 35%,#5b6470 60%,#a89a8c 100%)}

/* columns */
.col-head{top:373px;height:40px;background:var(--grey-dark);color:var(--white);text-align:center;font:700 18px/40px "Roboto Condensed",sans-serif;border-bottom:3px solid var(--panel)}
.col-body{top:413px;height:460px;background:var(--panel)}
.col-welcome{left:112px;width:224px}
.col-training{left:341px;width:215px}
.col-courses{left:561px;width:224px}
.col-training.col-head{font-size:15px}

.welcome-video{left:117px;top:425px;width:214px;height:130px;background:linear-gradient(135deg,#1b2a44 0%,#4d6d95 50%,#1d2b40 100%)}
.video-bar{left:117px;top:555px;width:214px;height:12px;background:#2b2b2b}
.video-bar i{position:absolute;left:16px;top:5px;width:120px;height:2px;background:#777}
.video-bar b{position:absolute;left:16px;top:5px;width:40px;height:2px;background:#c33}
.welcome-copy{left:118px;top:581px;width:213px;height:286px;overflow:hidden;font:400 8.6px/10.6px "Roboto",sans-serif;color:var(--ink);text-align:justify}
.welcome-copy p{text-indent:14px;margin-bottom:10px}

.menu-lead{left:341px;top:425px;width:215px;height:35px;background:var(--grey-dark);color:var(--green-pale);font:400 14px/35px "Roboto",sans-serif;padding-left:14px}
.menu-sub{left:341px;width:215px;background:#e4e4e4;border-top:1px solid var(--grey-line);padding:5px 12px;font:400 10px/1.25 "Roboto",sans-serif;color:var(--ink)}
.menu-sub b{display:block;font-weight:700}
.menu-btn{left:341px;width:215px;height:36px;background:var(--green);color:var(--white);font:400 14px/36px "Roboto",sans-serif;padding-left:12px}
.news-title{left:349px;top:730px;font:700 13.5px "Roboto Condensed",sans-serif;color:var(--ink)}
.news-item{left:349px;width:202px;font:400 8.8px/1.3 "Roboto",sans-serif;color:var(--ink);padding-bottom:8px;border-bottom:1px solid var(--grey-line)}
.news-item b{display:block;font:700 8.8px "Roboto",sans-serif;margin-bottom:3px}

.course{left:572px;width:196px;border-bottom:1px solid var(--grey-line);padding-bottom:10px}
.course h3{font:700 10px/1.35 "Roboto",sans-serif;color:var(--ink);margin-bottom:9px}
.course p{font:400 9px/1.35 "Roboto",sans-serif;color:var(--ink);margin-bottom:10px}
.course .places{font:700 10px "Roboto",sans-serif;color:var(--ink);margin-bottom:7px}
.course .book{width:80px;height:24px;background:var(--green);color:var(--white);font:700 10px/24px "Roboto",sans-serif;text-align:center}
.scroll-track{left:778px;top:425px;width:7px;height:443px;background:#e0e0e0}
.scroll-thumb{left:778px;top:448px;width:7px;height:38px;background:#555}

/* footer */
.footer{left:0;top:880px;width:900px;height:269px;background:#e8e8e8}
.footer-address{left:128px;top:902px;font:400 10.5px/1.45 "Roboto",sans-serif;color:var(--ink);font-style:normal}
.footer-links{top:902px;font:700 10.5px/1.7 "Roboto",sans-serif;color:var(--ink)}
.footer-links .hl{color:var(--green)}
.social{top:906px;width:24px;height:24px;border-radius:50%}
.badge{left:633px;top:935px;width:94px;height:62px;background:var(--white);border:1px solid var(--grey-line)}
.partners-label{left:127px;top:1015px;font:700 13px "Roboto",sans-serif;color:var(--ink)}
.partners-strip{left:93px;top:1040px;width:714px;height:92px;background:linear-gradient(#e8e8e8,#fff 30%,#fff 70%,#e8e8e8)}
.partner{top:1060px;height:48px;background:#9a9a9a}
.arrow{top:1064px}
.copyright{left:0;top:1149px;width:900px;height:51px;background:var(--grey-dark);color:var(--white);font:400 9px/51px "Roboto",sans-serif;padding-left:128px}
</style>
</head>
<body>

<!-- header -->
<div class="abs brand"><span class="brand-mark"></span><br>Marlow Vale<br>Teaching Alliance</div>

<div class="abs search-label">SEARCH SITE</div>
<div class="abs search-box">
  <svg width="14" height="14" viewBox="0 0 14 14"><circle cx="5.5" cy="5.5" r="4" fill="none" stroke="#222" stroke-width="1.8"/><line x1="8.5" y1="8.5" x2="13" y2="13" stroke="#222" stroke-width="2.2"/></svg>
</div>

<div class="abs live-chat">
  <svg width="34" height="38" viewBox="0 0 34 38"><circle cx="17" cy="15" r="11" fill="none" stroke="#222" stroke-width="2"/><path d="M6 16v6h4v-8H6z" fill="#222"/><path d="M10 24q4 6 10 5" fill="none" stroke="#222" stroke-width="1.5"/><rect x="8" y="32" width="18" height="5" fill="#222"/></svg>
  Live Chat
</div>

<div class="abs not-member">&lt;Not a member?&gt;</div>
<div class="abs register">REGISTER NOW</div>
<div class="abs btn-login">LOGIN</div>
<div class="abs email-box">YOUR E-MAIL</div>
<div class="abs btn-submit">SUBMIT</div>

<svg class="abs top-deco" width="160" height="22" viewBox="0 0 160 22">
  <polyline points="20,14 40,14 46,8 95,8 102,16 150,16" fill="none" stroke="#3cb46e" stroke-width="1"/>
  <path d="M12 0h16l-8 8z" fill="#3cb46e"/>
  <circle cx="95" cy="8" r="2" fill="#3cb46e"/>
  <circle cx="150" cy="16" r="2" fill="#3cb46e"/>
</svg>

<nav class="abs main-nav">
  <a class="active" style="left:16px">HOME</a>
  <a style="left:67px">ABOUT US</a>
  <a style="left:136px">TRAINING &amp; DEVELOPMENT</a>
  <a style="left:289px">BENEFITS</a>
  <a style="left:357px">MEMBERS</a>
  <a style="left:427px">WHAT'S ON</a>
  <a style="left:504px">CONTACT US</a>
  <a style="left:595px">NEWS</a>
  <a style="left:644px">FORUM</a>
</nav>

<!-- hero -->
<div class="abs page-band"></div>
<section class="abs hero-panel"></section>
<div class="abs hero-dots"><span></span><span class="on"></span><span></span><span></span></div>
<h1 class="abs hero-title">NEW TEACHERS IN&nbsp; WORKSHOP</h1>
<p class="abs hero-copy">Lorem ipsum dolor sit amet, consectetur adipiscing elit. Integer nec odio. Praesent libero. Sed cursus ante dapibus diam. Sed nisi. Nulla quis sem at nibh elementum imperdiet. Duis sagittis ipsum.<br>Sed dignissim lacinia nunc. Curabitur tortor. Pellentesque nibh. Aenean quam. In scelerisque sem at dolor.</p>
<div class="abs hero-more">&gt;&gt; FIND OUT MORE</div>
<div class="abs hero-photo" role="img" aria-label="Photo of a teacher at a laptop surrounded by students in a classroom workshop"></div>

<!-- column heads -->
<div class="abs col-head col-welcome">WELCOME</div>
<div class="abs col-head col-training">TRAINING &amp; DEVELOPMENT</div>
<div class="abs col-head col-courses">LATEST COURSES</div>
<div class="abs col-body col-welcome"></div>
<div class="abs col-body col-training"></div>
<div class="abs col-body col-courses"></div>

<!-- welcome -->
<div class="abs welcome-video" role="img" aria-label="Video still of a businessman sketching connected cloud and media icons"></div>
<div class="abs video-bar"><i></i><b></b></div>
<div class="abs welcome-copy">
  <p>From the beginning of the Teaching Schools' Programme, the 5 Lead Schools decided to work as a group together rather than as separate smaller groupings. Through this, we believe that we are far better placed to provide what the profession and the school system needs to develop and continue to develop. We are based across a wide geographical area with Lorem at its centre.</p>
  <p>Two Teaching School Alliances (Fenmoor Area Teaching Schools' Alliance and Fenmoor All-Through Teaching Schools' Alliance) are led by these Lead Schools working with about 30 partner schools. Some of these are our sponsored Academies. Others work in powerful partnership with us in various significant ways in different areas of the Teaching Schools' Programme.</p>
  <p>We have further strategic partners with whom we work closely in order to deliver Initial Teacher Training, Professional Development, School-to-school Support and Teacher Research.</p>
  <p>We have further strategic partners with whom we work closely in order to deliver Initial Teacher</p>
</div>

<!-- training -->
<div class="abs menu-lead">LEADERSHIP TRAINIG</div>
<div class="abs menu-sub" style="top:467px;height:48px"><b>MLDP</b>Middle Leadership Development Programme</div>
<div class="abs menu-sub" style="top:518px;height:36px"><b>OTP</b>Outstanding teacher programme</div>
<div class="abs menu-btn" style="top:559px">CPD</div>
<div class="abs menu-btn" style="top:600px">SCHOOL 2 SCHOOL SUPPORT</div>
<div class="abs menu-btn" style="top:641px">RESEARCH &amp; DEVELOPMENT</div>
<div class="abs menu-btn" style="top:684px">ITT (School direct)</div>

<h2 class="abs news-title">NEWS &amp; UPDATES</h2>
<div class="abs news-item" style="top:750px"><b>NEWS TITLE</b>Lorem ipsum dolor sit amet, usu id vero oratio adipisci. Ad lorem bonorum mei, tibique principes vix ea. Vidit eirmod evertitur te duo.</div>
<div class="abs news-item" style="top:814px"><b>NEWS TITLE</b>Lorem ipsum dolor sit amet, usu id vero oratio adipisci. Ad lorem bonorum mei, tibique principes vix ea. Vidit eirmod evertitur te duo.</div>

<!-- courses -->
<div class="abs course" style="top:428px">
  <h3>WANT TO DELIVER CONSINSTENLY OUTSTANDING LESSONS?</h3>
  <p>Lorem ipsum dolor sit amet, ut prima paulo argumentum cum, cu duo admodum malu isset. Lobortis eloquentiam id mei.</p>
  <div class="places">6 places left</div>
  <div class="book">BOOK</div>
</div>
<div class="abs course" style="top:579px">
  <h3>SCHOOL DIRECT INITIAL TEACHER TRAINING - Places still avaliable</h3>
  <p>Lorem ipsum dolor sit amet, ut prima paulo argumentum cum, cu duo admodum malu isset. Lobortis eloquentiam id mei.</p>
  <div class="places">2 places left</div>
  <div class="book">BOOK</div>
</div>
<div class="abs course" style="top:727px">
  <h3>TAKE A LOOK AT OUR NEWLY QUALIFIED TEACHERS LEARNING PACKAGES</h3>
  <p>Lorem ipsum dolor sit amet, ut prima paulo argumentum cum, cu duo admodum malu isset. Lobortis eloquentiam id mei.</p>
  <div class="places">10 places left</div>
  <div class="book">BOOK</div>
</div>
<div class="abs scroll-track"></div>
<div class="abs scroll-thumb"></div>

<!-- footer -->
<footer class="abs footer"></footer>
<address class="abs footer-address">Marlow Vale Teaching Alliance<br>Ashby Lane<br>Kelbridge<br>KB4 2LT<br>Tel: 01632 960418<br>email: info@marlowvaleteaching.co.uk</address>
<div class="abs footer-links" style="left:351px">About Us<br><span class="hl">Training &amp; Development</span><br>Benefits<br>Members<br>Calendars of Events</div>
<div class="abs footer-links" style="left:513px">Contact Us<br>News<br><span class="hl">Forum</span><br><br>Site map</div>
<div class="abs social" style="left:635px;background:#3b5b98"></div>
<div class="abs social" style="left:669px;background:#4aa8e0"></div>
<div class="abs badge"></div>

<div class="abs partners-label">Partner schools</div>
<div class="abs partners-strip"></div>
<svg class="abs arrow" style="left:74px" width="14" height="30" viewBox="0 0 14 30"><path d="M14 0v30L0 15z" fill="#333"/></svg>
<svg class="abs arrow" style="left:808px" width="14" height="30" viewBox="0 0 14 30"><path d="M0 0v30l14-15z" fill="#333"/></svg>
<div class="abs partner" style="left:108px;width:38px"></div>
<div class="abs partner" style="left:163px;width:38px;border-radius:4px"></div>
<div class="abs partner" style="left:218px;width:34px;border-radius:50%"></div>
<div class="abs partner" style="left:268px;width:32px"></div>
<div class="abs partner" style="left:315px;width:30px;border-radius:4px"></div>
<div class="abs partner" style="left:356px;width:118px"></div>
<div class="abs partner" style="left:478px;width:32px;border-radius:4px"></div>
<div class="abs partner" style="left:515px;width:36px;border-radius:50%"></div>
<div class="abs partner" style="left:560px;width:42px"></div>
<div class="abs partner" style="left:604px;width:48px"></div>
<div class="abs partner" style="left:656px;width:34px"></div>
<div class="abs partner" style="left:694px;width:92px"></div>

<div class="abs copyright">All Content Copyright 2012 - Northgate Studio. All Rights Reserved.</div>

</body>
</html>
```